R Hendrow tile

This add will be posted on a shopping cart at grocery store. I have limited space and need something to tie in all my info.Add will be top to bottom not horizontal
R. Hendrow
Custom Tile & Marble
"4 generations of Service"
Our slogan is: creating the most beautiful living spaces
614-283-7150
www.hendrowtile-example.com
email:rkbloom42@mailpost-example.com
in business since 1975
We would like to use the color yellow in the design and R. Hendrow has to be script font to match our trucks.

tile & marble flooring,walls, complete bathroom renovations new homes,remodels,

Shopping

ffc214
000000
b1b1b1
f37123

• Would like yellow to be used sparingly all other colors are just a suggestion. Need R. Hendrow To be in Script all other wording to be straight
• all contact info,other colors to tie into yellow

```html
<!DOCTYPE html>
<html lang="en">
<head>
<meta charset="utf-8">
<title>R. Hendrow Custom Tile &amp; Marble</title>
<link rel="stylesheet" href="https://fonts.googleapis.com/css2?family=Pinyon+Script&family=Tinos:wght@700&family=Arimo:wght@700&display=swap">
<style>
  :root {
    --yellow: #ffc214;
    --black: #000000;
    --grey: #b1b1b1;
    --orange: #f37123;
    --tile-light: #e4e2de;
    --tile-mid: #bdbbb6;
  }
  html, body {
    margin: 0;
    padding: 0;
    overflow: hidden;
    background: #ffffff;
  }
  .flyer {
    position: relative;
    width: 906px;
    height: 1200px;
    overflow: hidden;
    background: var(--yellow);
  }
  .flyer__backdrop {
    position: absolute;
    inset: 0;
  }
  .flyer__content {
    position: absolute;
    left: 0;
    right: 0;
    top: 560px;
    text-align: center;
  }
  .brand-name {
    margin: 0;
    font-family: "Pinyon Script", cursive;
    font-weight: 400;
    font-size: 104px;
    line-height: 1;
    color: var(--black);
    -webkit-text-stroke: 1.5px var(--orange);
    text-shadow: 3px 4px 6px rgba(160, 70, 0, 0.55);
  }
  .brand-trade {
    margin: 36px 0 0;
    font-family: "Tinos", serif;
    font-weight: 700;
    font-size: 52px;
    line-height: 1;
    color: var(--orange);
    letter-spacing: 0.5px;
  }
  .brand-motto {
    margin: 14px 0 0;
    font-family: "Arimo", sans-serif;
    font-weight: 700;
    font-size: 35px;
    line-height: 1;
    color: var(--black);
  }
  .slogan-band {
    margin-top: 22px;
    height: 80px;
    background: var(--black);
    display: flex;
    align-items: center;
    justify-content: center;
  }
  .slogan-band__text {
    font-family: "Pinyon Script", cursive;
    font-size: 44px;
    color: var(--orange);
    -webkit-text-stroke: 0.6px var(--orange);
  }
  .phone {
    margin: 20px 0 0;
    font-family: "Tinos", serif;
    font-weight: 700;
    font-size: 100px;
    line-height: 1;
    color: var(--black);
    letter-spacing: 1px;
  }
  .contact {
    margin: 40px 0 0;
    font-family: "Tinos", serif;
    font-weight: 700;
    font-size: 21px;
    line-height: 30px;
    color: var(--black);
  }
  .contact__social {
    display: inline-flex;
    align-items: center;
    gap: 4px;
  }
  .contact__social-mark {
    display: inline-block;
    width: 18px;
    height: 18px;
    background: var(--black);
    border-radius: 2px;
  }
  .since {
    margin: 6px 0 0;
    font-family: "Tinos", serif;
    font-weight: 700;
    font-size: 12px;
    color: var(--black);
  }
</style>
</head>
<body>
  <main class="flyer">
    <svg class="flyer__backdrop" width="906" height="1200" viewBox="0 0 906 1200" aria-hidden="false">
      <defs>
        <linearGradient id="bathroom-tones" x1="0" y1="0" x2="1" y2="0.3">
          <stop offset="0" stop-color="var(--tile-light)"/>
          <stop offset="0.5" stop-color="var(--tile-mid)"/>
          <stop offset="1" stop-color="#d6d5d2"/>
        </linearGradient>
      </defs>
      <rect class="hero-photo" x="0" y="0" width="906" height="520" fill="url(#bathroom-tones)" role="img" aria-label="Photo of a tiled bathroom with a recessed glass-shelf niche, stacked stone accent strip and rain shower head"/>
      <path class="hero-curve-edge" d="M0 478 C 260 520, 640 470, 906 322 L906 1200 L0 1200 Z" fill="var(--grey)"/>
      <path class="hero-curve-fill" d="M0 492 C 270 530, 650 480, 906 366 L906 1200 L0 1200 Z" fill="var(--yellow)"/>
    </svg>

    <section class="flyer__content">
      <h1 class="brand-name">R. Hendrow</h1>
      <p class="brand-trade">CUSTOM TILE &amp; MARBLE</p>
      <p class="brand-motto">"4 Generations of Service"</p>
      <div class="slogan-band">
        <span class="slogan-band__text">Creating the most beautiful living spaces</span>
      </div>
      <p class="phone">614-283-7150</p>
      <p class="contact">
        www.hendrowtile-example.com | rkbloom42@mailpost-example.com<br>
        <span class="contact__social">Like us on <span class="contact__social-mark"></span> hendrowtile</span>
      </p>
      <p class="since">in business since 1975</p>
    </section>
  </main>
</body>
</html>
```